Dovanne Luxury Landscapes

A landscape business card.

Target Market(s)

Middle aged and up. Professionals.

Industry/Entity Type

Landscape

Contact Information for Business Card

Waverley

Colors
0054AA
0677BA
7BADD7
CADEEF
E8F1F8
0094D4
00A9DD
6FCCEA
C7EBF8
E9F6FB

Requirements
Must have
• The color blue and silver be very attractive
Nice to have
• An embossed logo. A watermark of a plant or something that indicates that we are a landscape company in the background of the backside where list of services are offered. . List of services on the back.
Should not have
• Red, yellow, orange.

```html
<!DOCTYPE html>
<html lang="en">
<head>
<meta charset="UTF-8">
<title>Dovanne Luxury Landscapes – Business Card</title>
<link href="https://fonts.googleapis.com/css2?family=Marcellus&family=Poppins:wght@400&display=swap" rel="stylesheet">
<style>
  :root {
    --stage: #1f1f21;
    --card-blue: #2c43a0;
    --pattern-deep: #24358a;
    --pattern-light: #4a68e6;
    --silver: #c9ccd6;
    --white: #ffffff;
  }
  * { margin: 0; padding: 0; box-sizing: border-box; }
  html, body {
    width: 1200px; height: 1108px; overflow: hidden;
    background: var(--stage);
  }
  .stage {
    width: 1200px; height: 1108px;
    display: flex; align-items: center; justify-content: center; gap: 70px;
  }
  .card {
    width: 360px; height: 620px;
    border-radius: 22px;
    background: var(--card-blue);
    position: relative;
    overflow: hidden;
  }
  .card-front {
    display: flex; flex-direction: column; align-items: center;
    color: var(--silver);
    text-align: center;
    padding-top: 90px;
  }
  .brand-mark {
    width: 120px; height: 120px;
    border: 3px solid var(--silver);
    border-radius: 50%;
    margin-bottom: 34px;
  }
  .brand-name {
    font-family: "Marcellus", serif;
    font-size: 50px;
    letter-spacing: 2px;
    line-height: 1;
  }
  .brand-tagline {
    font-family: "Marcellus", serif;
    font-size: 20px;
    letter-spacing: 2px;
    margin-top: 10px;
  }
  .person-name {
    font-family: "Marcellus", serif;
    font-size: 25px;
    margin-top: 60px;
  }
  .divider {
    width: 92px; height: 2px;
    background: var(--silver);
    margin: 14px 0;
  }
  .contact {
    font-family: "Poppins", sans-serif;
    font-size: 17px;
    line-height: 1.5;
  }
  .card-back .pattern {
    position: absolute; inset: 0;
    background: linear-gradient(135deg, var(--pattern-light) 0%, var(--card-blue) 45%, var(--pattern-deep) 100%);
  }
  .card-back .back-name {
    position: absolute;
    right: 70px; bottom: 150px;
    font-family: "Marcellus", serif;
    font-size: 30px;
    color: var(--white);
  }
</style>
</head>
<body>
  <main class="stage">
    <section class="card card-front">
      <div class="brand-mark"></div>
      <div class="brand-name">DOVANNE</div>
      <div class="brand-tagline">LUXURY LANDSCAPES</div>
      <div class="person-name">MARLA KESSINGTON</div>
      <div class="divider"></div>
      <div class="contact">
        <p>902-555-0176</p>
        <p>www.dovanne.com</p>
      </div>
      <div class="divider"></div>
      <div class="contact">
        <p>18 Fernhill Lane, Alderbrook</p>
        <p>Harrow County, H4T 2K9.</p>
      </div>
    </section>
    <section class="card card-back">
      <div class="pattern" role="img" aria-label="Repeating embossed brand-mark pattern in tonal blues"></div>
      <div class="back-name">Dovanne</div>
    </section>
  </main>
</body>
</html>
```